Hypnosis signage

I need a signage 3.50 mt width x 1.60 length.
I'm attaching a signage.
But few changes the Text in the center slightly out of balance.
I'm attaching also photos that can go in one corner.
Please do keep the color orange
Updates

Please I need the signage in Arial Fonts with colors Orange and Black & White for letters or combination
is up to You .

Thank You
Dorian

Colors
f37022

Requirements
Must have
• Clinical Hypnosis
- Weight Loss
- Fear of
Public Speaking
- Anxiety
- Depression
- PTS
- Stop Smoking
- Confidence Building
- Alcohol Moderation

Book now: www.calmtidetrance.net
or call 9462 3089
Should not have
• do You guys see the letters on the signage? "Harbor Sparrows" if You can do the that with Weight Loss ,Stop Smoking, Fear Of Public Speaking , Alcohol Moderation . The letters a bit out of balance .

```html
<!DOCTYPE html>
<html lang="en">
<head>
<meta charset="utf-8">
<title>Clinical Hypnosis Signage</title>
<link href="https://fonts.googleapis.com/css2?family=Arimo:wght@400;700&display=swap" rel="stylesheet">
<style>
  :root {
    --orange: #f37022;
    --orange-deep: #e2531a;
    --yellow: #f4ea4a;
    --gold-line: #a7790e;
    --ink: #1a1410;
    --title-edge: #5a2a0c;
    --photo-warm: #e9a35a;
    --photo-green: #9fb06a;
  }
  * { margin: 0; padding: 0; box-sizing: border-box; }
  html, body { width: 1200px; height: 549px; overflow: hidden; background: #fff; }
  .sign {
    position: relative;
    width: 1200px;
    height: 549px;
    overflow: hidden;
    font-family: "Arimo", Arial, sans-serif;
  }
  .top-panel {
    position: absolute;
    left: 0; top: 0;
    width: 1200px; height: 380px;
    background: linear-gradient(90deg, #fbf7c8 0%, var(--yellow) 14%, #f2c236 34%, #f09a2c 52%, var(--orange) 70%, var(--orange-deep) 100%);
  }
  .photo {
    position: absolute;
    right: 0; top: 0;
    width: 440px; height: 378px;
    background:
      linear-gradient(90deg, rgba(240,140,50,1) 0%, rgba(240,140,50,0) 22%),
      radial-gradient(ellipse at 55% 55%, #f6efe6 0%, #e8cdb2 30%, rgba(233,163,90,0) 60%),
      linear-gradient(160deg, var(--photo-warm) 0%, #d99a4a 40%, var(--photo-green) 100%);
  }
  .title {
    position: absolute;
    left: 24px;
    color: var(--orange);
    font-weight: 700;
    -webkit-text-stroke: 2px var(--title-edge);
    text-shadow: 4px 5px 0 rgba(90,42,12,.55), 0 0 6px rgba(255,255,255,.6);
    line-height: 1;
    white-space: nowrap;
    transform-origin: left top;
  }
  .title-clinical { top: 102px; font-size: 94px; letter-spacing: 9px; }
  .title-hypnosis { top: 196px; left: 26px; font-size: 123px; transform: scaleX(0.74); }
  .services {
    position: absolute;
    left: 466px; top: 36px;
    list-style: none;
  }
  .services li {
    position: relative;
    padding-left: 23px;
    font-size: 26px;
    line-height: 36.2px;
    color: var(--ink);
  }
  .services li::before {
    content: "";
    position: absolute;
    left: 0; top: 10px;
    width: 16px; height: 16px;
    border-radius: 50%;
    background: radial-gradient(circle at 35% 30%, #ffe38a 0%, #f5a623 45%, #c96a08 100%);
  }
  .divider {
    position: absolute;
    left: 0; top: 376px;
    width: 1200px; height: 14px;
    background: linear-gradient(180deg, #f3c23a 0%, var(--gold-line) 45%, #d8a42a 100%);
  }
  .booking {
    position: absolute;
    left: 0; top: 390px;
    width: 1200px; height: 159px;
    background: var(--orange);
    color: var(--ink);
    font-weight: 700;
    text-align: center;
  }
  .booking-line {
    position: absolute;
    width: 100%;
    font-size: 60px;
    line-height: 1;
    transform: scaleX(0.88);
  }
  .booking-web { top: 16px; }
  .booking-call { top: 86px; }
</style>
</head>
<body>
  <div class="sign">
    <div class="top-panel"></div>
    <div class="photo" role="img" aria-label="Photo of a smiling mature couple embracing outdoors in autumn"></div>

    <div class="title title-clinical">Clinical</div>
    <div class="title title-hypnosis">Hypnosis</div>

    <ul class="services">
      <li>Weight Loss</li>
      <li>Fear of</li>
      <li>Public Speaking</li>
      <li>Anxiety</li>
      <li>Depression</li>
      <li>PTS</li>
      <li>Stop Smoking</li>
      <li>Confidence Building</li>
      <li>Alcohol Moderation</li>
    </ul>

    <div class="divider"></div>

    <div class="booking">
      <div class="booking-line booking-web">Book now: www.calmtidetrance.net</div>
      <div class="booking-line booking-call">or call 9462 3089</div>
    </div>
  </div>
</body>
</html>
```